Biz Card for Harrowfield Property Partners - HWPP

Harrowfield Property Partners is a commercial real estate acquisitions firm. We buy commercial property and need to raise capital from investors for each deal we buy. The vibe needs to be: give us your money, we will multiply it.
Our website: www.hrwpp-example.com
Competitors are: https://velmarholdings-example.com/, https://tribanquepartners-example.com/, http://www.ostrellecapital-example.com/
Target Market(s)
High Net Worth Individuals, Bankers, Insurance Companies, Commercial Real Estate Brokers.
Industry/Entity Type
Investment Banking
Contact Information for Business Card
Name, Title, Addess, Cell#, Office#, email, website
Requirements
Must have
- use one of our logos. See website for look and feel: www.hrwpp-example.com
Nice to have
- see website: www.hrwpp-example.com

```html
<!DOCTYPE html>
<html lang="en">
<head>
<meta charset="utf-8">
<title>Harrowfield Property Partners – Business Card</title>
<link rel="stylesheet" href="https://fonts.googleapis.com/css2?family=Montserrat:wght@400;500;600;700&display=swap">
<style>
  :root {
    --navy: #1b2a45;
    --slate: #7c8093;
    --white: #ffffff;
    --soft-white: #e9ebf0;
  }
  html, body {
    margin: 0;
    padding: 0;
    overflow: hidden;
    background: var(--navy);
  }
  .card {
    position: relative;
    width: 1200px;
    height: 686px;
    overflow: hidden;
    background: var(--navy);
    font-family: "Montserrat", sans-serif;
    color: var(--white);
  }
  .hero-art {
    position: absolute;
    left: 0;
    top: 0;
    width: 1200px;
    height: 686px;
  }
  .brand {
    position: absolute;
    left: 818px;
    top: 60px;
    display: flex;
    align-items: center;
    gap: 14px;
  }
  .brand-dot {
    width: 72px;
    height: 72px;
    border-radius: 50%;
    background: var(--white);
    flex: none;
  }
  .brand-name {
    font-weight: 600;
    font-size: 21px;
    line-height: 1.25;
    letter-spacing: 2px;
    color: var(--white);
    text-transform: uppercase;
  }
  .person-name {
    position: absolute;
    left: 773px;
    top: 180px;
    margin: 0;
    font-weight: 600;
    font-size: 38px;
    letter-spacing: 1px;
  }
  .name-rule {
    position: absolute;
    left: 766px;
    top: 238px;
    width: 377px;
    height: 3px;
    background: var(--white);
  }
  .job-title {
    position: absolute;
    left: 750px;
    top: 260px;
    margin: 0;
    font-weight: 500;
    font-size: 20px;
    letter-spacing: 2px;
    text-transform: uppercase;
  }
  .contact {
    position: absolute;
    margin: 0;
    text-align: right;
    white-space: nowrap;
  }
  .phone {
    font-weight: 400;
    font-size: 27px;
    color: var(--soft-white);
  }
  .phone-office { right: 84px; top: 338px; }
  .phone-cell { right: 70px; top: 396px; }
  .email {
    right: 73px;
    top: 450px;
    font-weight: 600;
    font-size: 28px;
  }
  .office-label {
    position: absolute;
    right: 103px;
    top: 536px;
    margin: 0;
    font-weight: 600;
    font-size: 28px;
  }
  .address {
    position: absolute;
    right: 110px;
    top: 578px;
    margin: 0;
    font-style: normal;
    font-weight: 400;
    font-size: 23px;
    line-height: 40px;
    text-align: right;
    color: var(--soft-white);
  }
  .address span { display: block; }
  .address .line-two { margin-right: 25px; }
</style>
</head>
<body>
  <main class="card">
    <svg class="hero-art" viewBox="0 0 1200 686" role="img" aria-label="Large lighthouse illustration on a grey disc">
      <circle cx="91" cy="274" r="606" fill="var(--slate)"/>
    </svg>

    <div class="brand">
      <span class="brand-dot"></span>
      <span class="brand-name">Harrowfield<br>Property Partners</span>
    </div>

    <h1 class="person-name">Dario L. Fenwick</h1>
    <div class="name-rule"></div>
    <p class="job-title">Director of Operations</p>

    <p class="contact phone phone-office">(555) 318-2094</p>
    <p class="contact phone phone-cell">(555) 318-2094</p>
    <p class="contact email">d.fenwick@hrwpp-example.com</p>

    <p class="office-label">USA Office</p>
    <address class="address">
      <span>480 Marlowe Ave, Suite 910</span>
      <span class="line-two">Westbrook Bay, FL 33190</span>
    </address>
  </main>
</body>
</html>
```